3 -4 PAGE GIFT CERTIFICATE REDEMPTION WEBSITE REVAMP

I am revamping the entire website at www.brightperkcentral.net

Will have brand new theme and new logo. Name Of Company:
Bonus Gratuity Dispatch Network
BGDN

OVERVIEW:
I NEED A 3-4 PAGE WEBSITE DESIGNED WITH CHECKOUT MODULE.
My company offers fully brandable and personalizable gift certificates good for travel, vacations, dining rewards, rebates, electronic gifts, etc. and I need to redesign the website where the fulfillment and redemption happens.

So the way it works is a business uses my online platform to create, brand and personalize these gift certificates. The business can brand the certificates in the upper right hand corner of each certificate where the “Compliments Of” area sits with their company logo, website, contact info, etc and can also personalize each individual gift certificate to a specific customer too. SEE EXAMPLE ATTACHED TO BRIEF.

The example I attached to this brief includes a logo which is really just a picture and under it there is 3 lines of text where the business can put a website, phone number and email.

On the left side of the top banner image you will see “Exclusively For”.

So now, after a customer enters their certificate ID #, the branding on the next page must match the Compliments Of area and also must personalize the Sales Page to the customer that is in the Exclusively For” area of the certificate…...

Page 1: LANDING PAGE
CONTENT:

Welcome to the online redemption source for vacation certificates, travel vouchers, digital electronic products, dining incentives, gas and grocery rewards and more!

ENTER YOUR CERTIFICATE ID #
ENTER YOUR EMAIL

Welcome to the online redemption system for vacation certificates, travel vouchers, rebates, digital products, dining incentives, gas and grocery rewards and more!

PLEASE ENTER A VALID CERTIFICATE ID NUMBER TO VIEW THE DETAILS AND TO REDEEM AND ACTIVATE YOUR SPECIAL OFFER.

Also we need a testimonial module ON THIS PAGE AND SALES PAGE

PAGE 2: SALES PAGE FOR OFFER (we will use the 1-4 Night Las Vegas Hotel Stay Certificate)
INSTRUCTIONS EXPLANATION FOR DESIGNER: Every gift certificate has a "Compliments Of Area" in the upper right hand corner....SEE SAMPLE ATTACHED TO BRIEF. On the sales page we also show this to the customer after they enter the code. Every certificate has a Compliments Of area and we will also add "Exclusively For" so the person that is giving the certificate away can specify the name of the recipient so we will also transffer this information over to the SALES PAGE.

CONTENT FOR SALES PAGE:

WELCOME ~~NAME OF PERSON IN EXCLUSIVELY FOR AREA ON CERTIFICATE~~ !!

THIS SPECIAL INCENTIVE OFFER IS COMPLIMENTS OF

~~LOGO THAT IS SEEN ON CERTIFICATE~~
~~TEXT LINE 1~~
~~TEXT LINE 2~~
~~TEXT LINE 3~~

TITLE OF OFFER: STAY & PLAY IN LAS VEGAS FOR UP TO 4 NIGHTS!
There is no doubt that Las Vegas is one of the hottest travel destinations around the world. In fact, some people would even go as far as saying that perhaps it is THE hottest place to visit. Enjoy up to 4 nights of resort/casino accommodations in exciting Las Vegas, NV. Millions of people travel to this exciting city each year to enjoy its thrills. Thanks to the business you received this certificate from, now you can enjoy Las Vegas, NV too!

Features:
*Travel 7 Days A Week
*Stay Your Choice Of Nights (1-4 Nights)
*Good For Two Adults & Two Children
*Pay Just The Taxes & Fees
*Multiple Travel Date Requests Allowed
*Fully Transferable To Another Person
*Just A 30 Days Advance Notice Required
*You Will Have 12 Months To Complete Travel

HOW CAN WE DO THIS?

We contract with the world leading hotel chains and resorts to help them fill their otherwise empty rooms.

We help fill empty rooms which the hotels, resorts and cruise lines turn into additional revenue from other areas of their property and future bookings.

Hotels rarely experience full occupancy, yet they remain open, providing rooms and services at fixed costs. So when hotels give out their rooms by partnering with marketing companies like us, they might miss out on the room fee, but they already didn't have that in the first place, at least now they have the opportunity to gain a customer for their in-house restaurants, room service, their casinos, an extra day stay, future bookings, etc.

The magic of why our program works so well is the fact that it’s a win win for everyone involved. You win because you received a huge savings. The business who gave you the certificate wins because now you will remember them the next time you need the same kind of product or service that they provide and you might even refer your friends and family members. The hotels and resorts win because they gain additional revenue from other areas of their establishment that they otherwise would not have been able to get and they also have a new client that may book with them in the future. Remember, they didn’t have anyone in the room in the first place so since you are paying the normal rack rate you might be more inclined to spend your money at the hotel. You are never under any obligation to do so though!

Retail Value: Up to $826.00 (based on $159.00 per night)

How it Works:
You will receive up to 4 nights in a 3 star or better Las Vegas resort and casino for up to 4 travelers, 2 adults and 2 children.

Simply redeem the certificate to activate the travel period for 1 year. This means you will have at least 1 year to travel from the date you redeem and activate your offer. Be sure to redeem your certificate before it expires! All certificates will have an accompanying expiration date attached to them.

When you are ready to book you will simply have to pay the daily room rate taxes and fees of approximately $12-$33 per night (not per person). On average the taxes and fees come out to about $19 per night. (Retail Value: Up to $826.00 based on $159.00 per night)

Step 1: Redeem your certificate to activate your offer

Step 2: Fill out the online reservation request form with travel dates within the next 12 months.

Step 3: Wait for a confirmation of your booked reservation. You will be notified immediately upon us booking your reservation.

Go on your vacation and thank the business who gave you this special offer by doing business with them again and referring your friends and family members!

No timeshares or sales presentations, Guaranteed!

PAGE 3 IS CHECKOUT PAGE:

PLEASE USE ****HERE IS SAMPLE CODE FOR YOU TO TEST OUT AT CURRENT REDEMPTION PROCESS WWW.BRIGHTPERKCENTRAL.NET 40613-27149

TO SEE THE CURRENT CHECK OUT. I NEED ALL THE SAME CONTENT JUST A DIFFERENT MORE EFFICIENT CHECKOUT PROCESS HERE. OMIT THE LEFT SIDE OF THE CURRENT CHECK OUT PROCESS AS THIS CURRENT PROCESSS IS ONE STEP AND DOES NOT HAVE A SALES PAGE BUT NOW I AM CREATING A SALES PAGE BEFORE THE CHECKOUT SO THE BRANDING AND PERSONALIZATION WILL HAPPEN ON THE SALES PAGE….THANK YOU

Target Market(s)

END USERS THAT ARE REDEEMING SPECIAL OFFERS GIFT CERTIFICATES

Industry/Entity Type

Marketing

Number of Pages Required

4 page

Colors

Designer to choose colors to be used in the design.

Requirements
Must have
• OVERVIEW:
• I NEED A 3-4 PAGE WEBSITE DESIGNED WITH CHECKOUT MODULE.
• My company offers fully brandable and personalizable gift certificates good for travel, vacations, dining rewards, rebates, electronic gifts, etc. and I need to redesign the website where the fulfillment and redemption happens.
• So the way it works is a business uses my online platform to create, brand and personalize these gift certificates. The business can brand the certificates in the upper right hand corner of each certificate where the “Compliments Of” area sits with their company logo, website, contact info, etc and can also personalize each individual gift certificate to a specific customer too. SEE EXAMPLE ATTACHED TO BRIEF.
• The example I attached to this brief includes a logo which is really just a picture and under it there is 3 lines of text where the business can put a website, phone number and email.
• On the left side of the top banner image you will see “Exclusively For”.
• So now, after a customer enters their certificate ID #, the branding on the next page must match the Compliments Of area and also must personalize the Sales Page to the customer that is in the Exclusively For” area of the certificate…...
• Page 1: LANDING PAGE
• CONTENT:
• Welcome to the online redemption source for vacation certificates, travel vouchers, digital electronic products, dining incentives, gas and grocery rewards and more!
• ENTER YOUR CERTIFICATE ID #
• ENTER YOUR EMAIL
• Welcome to the online redemption system for vacation certificates, travel vouchers, rebates, digital products, dining incentives, gas and grocery rewards and more!
• PLEASE ENTER A VALID CERTIFICATE ID NUMBER TO VIEW THE DETAILS AND TO REDEEM AND ACTIVATE YOUR SPECIAL OFFER.
• Also we need a testimonial module ON THIS PAGE AND SALES PAGE
• PAGE 2: SALES PAGE FOR OFFER (we will use the 1-4 Night Las Vegas Hotel Stay Certificate)
• INSTRUCTIONS EXPLANATION FOR DESIGNER: Every gift certificate has a "Compliments Of Area" in the upper right hand corner....SEE SAMPLE ATTACHED TO BRIEF. On the sales page we also show this to the customer after they enter the code. Every certificate has a Compliments Of area and we will also add "Exclusively For" so the person that is giving the certificate away can specify the name of the recipient so we will also transffer this information over to the SALES PAGE.
• CONTENT FOR SALES PAGE:
• WELCOME ~~NAME OF PERSON IN EXCLUSIVELY FOR AREA ON CERTIFICATE~~ !!
• THIS SPECIAL INCENTIVE OFFER IS COMPLIMENTS OF
• ~~LOGO THAT IS SEEN ON CERTIFICATE~~
• ~~TEXT LINE 1~~
• ~~TEXT LINE 2~~
• ~~TEXT LINE 3~~
• TITLE OF OFFER: STAY & PLAY IN LAS VEGAS FOR UP TO 4 NIGHTS!
• There is no doubt that Las Vegas is one of the hottest travel destinations around the world. In fact, some people would even go as far as saying that perhaps it is THE hottest place to visit. Enjoy up to 4 nights of resort/casino accommodations in exciting Las Vegas, NV. Millions of people travel to this exciting city each year to enjoy its thrills. Thanks to the business you received this certificate from, now you can enjoy Las Vegas, NV too!
• Features:
• *Travel 7 Days A Week
• *Stay Your Choice Of Nights (1-4 Nights)
• *Good For Two Adults & Two Children
• *Pay Just The Taxes & Fees
• *Multiple Travel Date Requests Allowed
• *Fully Transferable To Another Person
• *Just A 30 Days Advance Notice Required
• *You Will Have 12 Months To Complete Travel
• HOW CAN WE DO THIS?
• We contract with the world leading hotel chains and resorts to help them fill their otherwise empty rooms.
• We help fill empty rooms which the hotels, resorts and cruise lines turn into additional revenue from other areas of their property and future bookings.
• Hotels rarely experience full occupancy, yet they remain open, providing rooms and services at fixed costs. So when hotels give out their rooms by partnering with marketing companies like us, they might miss out on the room fee, but they already didn't have that in the first place, at least now they have the opportunity to gain a customer for their in-house restaurants, room service, their casinos, an extra day stay, future bookings, etc.
• The magic of why our program works so well is the fact that it’s a win win for everyone involved. You win because you received a huge savings. The business who gave you the certificate wins because now you will remember them the next time you need the same kind of product or service that they provide and you might even refer your friends and family members. The hotels and resorts win because they gain additional revenue from other areas of their establishment that they otherwise would not have been able to get and they also have a new client that may book with them in the future. Remember, they didn’t have anyone in the room in the first place so since you are paying the normal rack rate you might be more inclined to spend your money at the hotel. You are never under any obligation to do so though!
• Retail Value: Up to $826.00 (based on $159.00 per night)
• How it Works:
• You will receive up to 4 nights in a 3 star or better Las Vegas resort and casino for up to 4 travelers, 2 adults and 2 children.
• Simply redeem the certificate to activate the travel period for 1 year. This means you will have at least 1 year to travel from the date you redeem and activate your offer. Be sure to redeem your certificate before it expires! All certificates will have an accompanying expiration date attached to them.
• When you are ready to book you will simply have to pay the daily room rate taxes and fees of approximately $12-$33 per night (not per person). On average the taxes and fees come out to about $19 per night. (Retail Value: Up to $826.00 based on $159.00 per night)
• Step 1: Redeem your certificate to activate your offer
• Step 2: Fill out the online reservation request form with travel dates within the next 12 months.
• Step 3: Wait for a confirmation of your booked reservation. You will be notified immediately upon us booking your reservation.
• Go on your vacation and thank the business who gave you this special offer by doing business with them again and referring your friends and family members!
• No timeshares or sales presentations, Guaranteed!
• PAGE 3 IS CHECKOUT PAGE:
• PLEASE USE ****HERE IS SAMPLE CODE FOR YOU TO TEST OUT AT CURRENT REDEMPTION PROCESS WWW.BRIGHTPERKCENTRAL.NET 40613-27149
• TO SEE THE CURRENT CHECK OUT. I NEED ALL THE SAME CONTENT JUST A DIFFERENT MORE EFFICIENT CHECKOUT PROCESS HERE. OMIT THE LEFT SIDE OF THE CURRENT CHECK OUT PROCESS AS THIS CURRENT PROCESSS IS ONE STEP AND DOES NOT HAVE A SALES PAGE BUT NOW I AM CREATING A SALES PAGE BEFORE THE CHECKOUT SO THE BRANDING AND PERSONALIZATION WILL HAPPEN ON THE SALES PAGE….THANK YOU
Nice to have
• OVERVIEW:
• Page 1: LANDING PAGE
• CONTENT:
• ENTER YOUR EMAIL
• CONTENT FOR SALES PAGE:
• ~~TEXT LINE 1~~
• ~~TEXT LINE 2~~
• ~~TEXT LINE 3~~
• Features:
• *Travel 7 Days A Week
• HOW CAN WE DO THIS?
• How it Works:
Should not have
• OVERVIEW:
• Page 1: LANDING PAGE
• CONTENT:
• ENTER YOUR EMAIL
• CONTENT FOR SALES PAGE:
• ~~TEXT LINE 1~~
• ~~TEXT LINE 2~~
• ~~TEXT LINE 3~~
• Features:
• *Travel 7 Days A Week
• HOW CAN WE DO THIS?
• How it Works:

```html
<!DOCTYPE html>
<html lang="en">
<head>
<meta charset="utf-8">
<title>Bonus Gratuity Dispatch Network – Online Redemption</title>
<link rel="stylesheet" href="https://fonts.googleapis.com/css2?family=Montserrat:ital,wght@0,400;0,500;0,600;0,700;0,800;1,400&display=swap">
<style>
:root{
  --sky:#1a73d6;
  --sky-deep:#0d5bbf;
  --sea:#2bb3a8;
  --jungle:#2f6d3a;
  --teal:#2fa982;
  --teal-dark:#24906d;
  --ink:#111111;
  --text:#333333;
  --muted:#8a8a8a;
  --line:#dddddd;
  --paper:#ffffff;
  --soft:#f5f5f3;
  --night:#050505;
}
*{box-sizing:border-box;margin:0;padding:0}
html,body{width:1200px;height:2287px;overflow:hidden}
body{position:relative;background:var(--paper);font-family:"Montserrat",sans-serif;color:var(--text)}
.abs{position:absolute}

/* hero */
.hero{left:0;top:0;width:1200px;height:700px;
  background:
   linear-gradient(180deg,var(--sky) 0,var(--sky) 118px,#4f93cf 124px,#8fb7d3 190px,#3d7a5a 300px,#2d6a44 420px,#2aa9a0 520px,#43c2b3 620px,#7fd1c2 700px)}
.hero-band{left:0;top:0;width:1200px;height:123px;background:linear-gradient(90deg,#1667d0,#1f7ee0 55%,#1a74da)}
.brand{left:90px;top:26px;color:#fff;font-weight:700;font-variant:small-caps;line-height:1.15;text-align:center}
.brand .l1{font-size:31px;letter-spacing:.5px}
.brand .l2{font-size:22px;letter-spacing:.5px}
.topnav{right:90px;top:40px;display:flex;align-items:center;gap:22px;color:#fff;font-size:15px;letter-spacing:.3px}
.topnav .item{display:flex;align-items:center;gap:8px}
.avatar-sm{width:32px;height:32px;border-radius:50%;background:#c99a7d;border:2px solid rgba(255,255,255,.6)}
.heart{width:34px;height:34px;border-radius:50%;background:rgba(255,255,255,.2);display:flex;align-items:center;justify-content:center}
.hero-title{left:0;width:1200px;top:226px;text-align:center;color:#fff;font-weight:700;font-size:54px;line-height:1.0;text-shadow:0 2px 6px rgba(0,0,0,.25)}
.hero-sub{left:0;width:1200px;top:354px;text-align:center;color:#fff;font-weight:600;font-size:19px;line-height:1.6;text-shadow:0 1px 4px rgba(0,0,0,.35)}
.field{top:443px;height:50px;width:290px;border-radius:25px;background:rgba(10,25,30,.78);color:#fff;font-size:15px;padding:0 20px;display:flex;align-items:center}
.go{left:850px;top:443px;width:101px;height:50px;border-radius:25px;background:var(--teal);color:#fff;font-weight:700;font-size:22px;display:flex;align-items:center;justify-content:center}
.wave{left:0;top:600px;width:1200px;height:110px}

/* categories */
.cat{top:745px;width:200px;text-align:center;color:var(--muted);font-size:16px;line-height:1.4}
.cat svg{display:block;margin:0 auto 14px}
.sep{top:748px;width:1px;height:104px;background:var(--line)}
.feature-card{left:729px;top:631px;width:217px;height:247px;background:#fff;box-shadow:0 4px 14px rgba(0,0,0,.12);text-align:center}
.feature-card .ph{width:217px;height:167px;background:linear-gradient(180deg,#6c5a4a,#3a2f27 55%,#8a7a6c)}
.feature-card .lbl{padding-top:16px;color:var(--ink);font-weight:600;font-size:16px;line-height:1.4}
.redeem{left:445px;top:922px;width:309px;height:51px;border-radius:26px;background:var(--teal);color:#fff;font-weight:600;font-size:17px;display:flex;align-items:center;justify-content:center;gap:10px;box-shadow:0 5px 10px rgba(0,0,0,.18)}

/* testimonials */
.testimonials{left:0;top:1075px;width:1200px;height:636px;background:var(--soft)}
.sec-title{left:0;width:1200px;text-align:center;color:var(--ink);font-weight:700;font-size:41px}
.tcard{top:1228px;height:378px;background:#fff;box-shadow:0 2px 8px rgba(0,0,0,.06)}
.tcard .ph{position:relative;height:284px;display:flex;align-items:flex-end;padding:18px 18px 20px;color:#fff;font-size:14.5px;line-height:1.75}
.tcard .ph::before{content:"";position:absolute;inset:0;background:linear-gradient(180deg,rgba(0,0,0,0) 30%,rgba(0,0,0,.6))}
.tcard .ph span{position:relative}
.who{display:flex;gap:12px;padding:16px 10px 0}
.who .av{width:42px;height:42px;border-radius:50%;background:#c9a086;flex:none}
.who .nm{color:var(--ink);font-size:15px;padding-top:3px}
.who .pl{color:var(--muted);font-style:italic;font-size:14px;margin-top:2px}
.added{padding:10px 10px 0;font-size:10.5px;color:#444}
.arrow{top:1420px;width:16px;height:16px}

/* clients */
.clients-sub{left:0;width:1200px;top:1866px;text-align:center;color:var(--ink);font-size:18px;font-weight:500}
.client{top:1936px;height:30px;display:flex;align-items:center;gap:7px;color:#6f6f6f;font-weight:600;font-size:18px}
.client i{display:block;width:14px;height:14px;border-radius:50%;background:#9a9a9a}

/* footer */
.foot-wave{left:0;top:2060px;width:1200px;height:70px}
.footer{left:0;top:2126px;width:1200px;height:161px;background:var(--night)}
.foot-brand{left:0;width:1200px;top:2162px;text-align:center;color:#fff;font-weight:700;font-variant:small-caps;line-height:1.15}
.foot-brand .l1{font-size:31px}
.foot-brand .l2{font-size:22px}
.copy{left:0;width:1200px;top:2244px;text-align:center;color:#fff;font-size:14px}
.code{right:22px;top:2246px;color:#fff;font-size:11px}
</style>
</head>
<body>

<div class="abs hero" role="img" aria-label="Tropical bay with limestone cliffs, turquoise water and longtail boats on a beach"></div>
<div class="abs hero-band"></div>

<div class="abs brand"><div class="l1">Bonus Gratuity</div><div class="l2">Dispatch Network</div></div>

<nav class="abs topnav">
  <div class="item"><div class="avatar-sm" role="img" aria-label="Account profile photo"></div>MY ACCOUNT</div>
  <div class="heart"><svg width="16" height="16" viewBox="0 0 24 24" fill="none" stroke="#fff" stroke-width="2"><path d="M12 20s-7-4.5-7-10a4 4 0 0 1 7-2.5A4 4 0 0 1 19 10c0 5.5-7 10-7 10z"/></svg></div>
  <div class="item"><svg width="20" height="18" viewBox="0 0 20 18"><rect x="1" y="5" width="18" height="12" rx="2" fill="#f6c342"/><path d="M10 5v12M1 9h18" stroke="#e88a2a" stroke-width="2"/></svg>GIFT CERTIFICATE</div>
</nav>

<h1 class="abs hero-title">Welcome to the Online<br>Redemption Source</h1>
<p class="abs hero-sub">Please Enter A Valid Certificate Id Number To View The Details And To<br>Redeem And Activate Your Special Offer.</p>

<div class="abs field" style="left:248px">Certificate ID</div>
<div class="abs field" style="left:549px">Enter Your Email Id</div>
<div class="abs go">Go</div>

<svg class="abs wave" viewBox="0 0 1200 110" preserveAspectRatio="none">
  <path d="M0 72 C220 30 420 55 620 88 C820 120 1000 90 1200 25 L1200 110 L0 110Z" fill="var(--sea)"/>
  <path d="M0 78 C220 38 420 62 620 95 C820 125 1000 98 1200 32 L1200 110 L0 110Z" fill="#fff"/>
</svg>

<!-- categories -->
<div class="abs cat" style="left:32px">
  <svg width="52" height="52" viewBox="0 0 52 52" fill="none" stroke="#9a9a9a" stroke-width="1.5"><rect x="2" y="4" width="48" height="34"/><rect x="6" y="8" width="40" height="26"/><path d="M12 16h28M12 22h20"/><circle cx="32" cy="36" r="6"/><path d="M29 41l-2 9 5-3 5 3-2-9"/></svg>
  Vacation<br>Certificates
</div>
<div class="abs sep" style="left:247px"></div>
<div class="abs cat" style="left:262px">
  <svg width="52" height="52" viewBox="0 0 52 52" fill="none" stroke="#9a9a9a" stroke-width="1.5"><rect x="2" y="18" width="48" height="30"/><path d="M10 18l26-14 8 14"/><path d="M8 30l6 8M8 38l6-8M20 30h24M20 36h24M20 42h16"/></svg>
  Travel<br>Vouchers
</div>
<div class="abs sep" style="left:458px"></div>
<div class="abs cat" style="left:493px">
  <svg width="52" height="52" viewBox="0 0 52 52" fill="none" stroke="#9a9a9a" stroke-width="1.5"><rect x="14" y="2" width="24" height="48" rx="8"/><rect x="2" y="10" width="48" height="32" rx="10"/><circle cx="14" cy="26" r="7"/><path d="M14 22v4h3"/><circle cx="44" cy="20" r="1.5"/><circle cx="44" cy="26" r="1.5"/><circle cx="44" cy="32" r="1.5"/></svg>
  Digital<br>Electronic Products
</div>
<div class="abs feature-card">
  <div class="ph" role="img" aria-label="Cosy dining room with wooden chairs and hanging lights"></div>
  <div class="lbl">Dining<br>Incentives</div>
</div>
<div class="abs cat" style="left:955px">
  <svg width="52" height="52" viewBox="0 0 52 52" fill="none" stroke="#9a9a9a" stroke-width="1.5"><path d="M4 4h44v6H4zM2 10h48v8H2z"/><path d="M5 18v30h42V18"/><rect x="10" y="26" width="12" height="22"/><rect x="27" y="26" width="14" height="14"/><path d="M29 38l10-10"/></svg>
  Gas &amp; Grocery<br>Rewards
</div>

<div class="abs redeem">Redeem Your Offer Now
  <svg width="18" height="18" viewBox="0 0 18 18"><circle cx="9" cy="9" r="8" fill="#fff"/><path d="M5 9h7M9 5.5L12.5 9 9 12.5" stroke="var(--teal)" stroke-width="2" fill="none"/></svg>
</div>

<!-- testimonials -->
<section class="abs testimonials"></section>
<h2 class="abs sec-title" style="top:1158px">Testimonials</h2>

<svg class="abs arrow" style="left:77px" viewBox="0 0 16 16"><path d="M10 3L5 8l5 5" stroke="#555" stroke-width="1.6" fill="none"/></svg>
<svg class="abs arrow" style="left:1107px" viewBox="0 0 16 16"><path d="M6 3l5 5-5 5" stroke="#555" stroke-width="1.6" fill="none"/></svg>

<article class="abs tcard" style="left:141px;width:289px">
  <div class="ph" role="img" aria-label="Traveller in a boat among limestone islands" style="background:linear-gradient(180deg,#8fa7b0,#4e6b58 45%,#2f5560)"><span>“I worked with the travel agency and they were very patient with me as I narrowed down where myself and another friend wanted to travel to…”</span></div>
  <div class="who"><div class="av" role="img" aria-label="Reviewer photo"></div><div><div class="nm">Mason T.</div><div class="pl">Duluth, GA</div></div></div>
  <div class="added">Added on 01/21/2020 09:27:24 pm</div>
</article>
<article class="abs tcard" style="left:452px;width:297px">
  <div class="ph" role="img" aria-label="City skyline and riverboat at night" style="background:linear-gradient(180deg,#1d3f70,#2a4c78 40%,#6a5a40 62%,#141820)"><span>"The travel agency did an excellent job booking my trip to Nashville. "</span></div>
  <div class="who"><div class="av" role="img" aria-label="Reviewer photo" style="background:#b88a6a"></div><div><div class="nm">Roland K.</div><div class="pl">North Las Vegas, NV</div></div></div>
  <div class="added">Added on 01/21/2020 09:19:30 pm</div>
</article>
<article class="abs tcard" style="left:770px;width:289px;border-bottom-right-radius:28px">
  <div class="ph" role="img" aria-label="Elegant hotel lobby with chandelier" style="background:linear-gradient(180deg,#6d5135,#a7875e 40%,#5a4430)"><span>“Wonderful! It was just like being in Rome, but only with great shows to enjoy. The rooms of the Castellan and service were excellent.”</span></div>
  <div class="who"><div class="av" role="img" aria-label="Reviewer photo" style="background:#8fa3b5"></div><div><div class="nm">Derek L.</div><div class="pl">Flagstaff, AZ</div></div></div>
  <div class="added">Added on 01/21/2020 09:03:06 pm</div>
</article>

<!-- clients -->
<h2 class="abs sec-title" style="top:1806px">Our Clients</h2>
<p class="abs clients-sub">A few of our clients that we redeem and fulfill gift certificates and rewards for</p>
<div class="abs client" style="left:150px">Palmwave</div>
<div class="abs client" style="left:328px"><i></i>Swiftpay</div>
<div class="abs client" style="left:522px"><i></i>Mockworks</div>
<div class="abs client" style="left:755px">Gladpatron</div>
<div class="abs client" style="left:932px"><i></i>Talkbridge</div>

<!-- footer -->
<svg class="abs foot-wave" viewBox="0 0 1200 70" preserveAspectRatio="none">
  <path d="M0 12 C180 45 420 55 640 28 C860 2 1040 10 1200 70 L1200 70 L0 70Z" fill="var(--sea)"/>
  <path d="M0 18 C180 52 420 62 640 36 C860 10 1040 18 1200 76 L1200 70 L0 70Z" fill="var(--night)"/>
</svg>
<footer class="abs footer"></footer>
<div class="abs foot-brand"><div class="l1">Bonus Gratuity</div><div class="l2">Dispatch Network</div></div>
<p class="abs copy">© Copyright 2020 The Company name. All Rights Reserved.</p>
<span class="abs code">C28</span>

</body>
</html>
```